Text Box for making an update on our website

We need an awesome "Text Box" so that our Users can make an amazing Post or update on our website or App.

Let's make something super duper like Pictavo, Friendloop, Chirr or Qmeld text box but a bit more amazing....

I've included our current desktop and Mobile "Text Box" which needs love :)

Our Text Box by default makes a Post "Private" the User can change it to "Public"

I have included what a final "Post" looks like on our site.

Could we incorporate a bit of the "Post" design into the "Create Post" design..... maybe make the header similar.

thanks

Morgan

Target Market(s)

Health Care, Hospitals, Caregivers, Nurses

Industry/Entity Type

Health Care

Font styles to use
Other font styles liked:
• Comfortaa

Requirements
Must have
• Our main colors are

#1D44B8 - Blue
#D85097 - Pink
Nice to have
• Super clean and simple. Happy and Easy to use
Should not have
• Complicated

Too many colors

```html
<!DOCTYPE html>
<html lang="en">
<head>
<meta charset="utf-8">
<title>Create Post</title>
<link rel="stylesheet" href="https://fonts.googleapis.com/css2?family=Comfortaa:wght@400;500;700&display=swap">
<style>
  :root{
    --page:#fafafa;
    --dim-top:#8a8a8a;
    --header-dim:#23457a;
    --title-dim:#7b808b;
    --brand-blue:#2f4cb8;
    --brand-pink:#d85097;
    --mark-dim:#7a3a63;
    --pill:#e7eaf6;
    --placeholder:#8fa0e0;
    --icon-blue:#2f55b8;
    --white:#ffffff;
  }
  *{box-sizing:border-box;margin:0;padding:0}
  html,body{width:1129px;height:1200px;overflow:hidden}
  body{background:var(--page);font-family:"Comfortaa",sans-serif;position:relative}
  .backdrop-strip{position:absolute;left:0;top:0;width:1129px;height:60px;background:var(--dim-top)}
  .post-card{position:absolute;left:0;top:25px;width:1129px;height:700px;border-radius:55px 55px 0 0;overflow:hidden;background:var(--header-dim)}
  .post-header{position:absolute;left:0;top:0;width:100%;height:177px;background:var(--header-dim)}
  .author-badge{position:absolute;left:52px;top:22px;width:60px;height:100px;background:var(--mark-dim);border-radius:0 0 0 40px}
  .author-avatar{position:absolute;left:88px;top:22px;width:112px;height:112px;border-radius:50%;background:radial-gradient(circle at 50% 40%,#c9a48a,#6b4a3a 70%,#2a2a2a)}
  .author-name{position:absolute;left:222px;top:58px;font-size:46px;font-weight:700;color:var(--title-dim);letter-spacing:.5px}
  .org-mark{position:absolute;left:992px;top:46px;width:84px;height:84px;border-radius:50%;background:var(--mark-dim)}
  .post-photo{position:absolute;left:0;top:177px;width:100%;height:523px;background:radial-gradient(ellipse at 55% 50%,#6e4f40 0%,#3a2d28 45%,#1f2224 100%)}
  .compose-sheet{position:absolute;left:0;top:678px;width:1129px;height:170px;background:var(--brand-blue);border-radius:0 0 55px 55px;box-shadow:0 6px 14px rgba(0,0,0,.25)}
  .sheet-handle{position:absolute;left:530px;top:22px;width:71px;height:8px;border-radius:4px;background:#c9d0ee}
  .close-btn{position:absolute;left:55px;top:66px;width:42px;height:42px}
  .sheet-title{position:absolute;left:0;width:1129px;top:60px;text-align:center;font-size:52px;font-weight:700;color:var(--white)}
  .visibility-toggle{position:absolute;left:813px;top:31px;width:286px;height:112px;border-radius:56px;background:var(--pill)}
  .visibility-label{position:absolute;left:27px;top:32px;font-size:43px;font-weight:500;color:var(--brand-pink)}
  .visibility-dot{position:absolute;left:197px;top:21px;width:70px;height:70px;border-radius:50%;background:var(--brand-pink)}
  .post-input{position:absolute;left:20px;top:867px;width:1083px;height:183px;border:2px solid var(--brand-pink);border-radius:16px;background:var(--page)}
  .caret{position:absolute;left:48px;top:24px;width:4px;height:46px;background:#4d7be0;border-radius:2px}
  .placeholder{position:absolute;left:52px;top:22px;font-size:43px;color:var(--placeholder)}
  .expand-icon{position:absolute;left:1020px;top:122px;width:42px;height:42px}
  .tool{position:absolute}
  .tool-media{left:46px;top:1085px}
  .tool-place{left:172px;top:1083px}
  .tool-tag{left:280px;top:1086px}
  .send-btn{position:absolute;left:970px;top:1071px;width:106px;height:106px;border-radius:50%;background:var(--brand-blue);box-shadow:0 4px 10px rgba(0,0,0,.2)}
  .send-btn svg{position:absolute;left:26px;top:26px}
</style>
</head>
<body>
  <div class="backdrop-strip"></div>

  <article class="post-card">
    <header class="post-header">
      <div class="author-badge"></div>
      <div class="author-avatar" role="img" aria-label="Author profile photo"></div>
      <div class="author-name">Kind Harbor Center</div>
      <div class="org-mark"></div>
    </header>
    <div class="post-photo" role="img" aria-label="Post photo of a smiling woman"></div>
  </article>

  <section class="compose-sheet">
    <div class="sheet-handle"></div>
    <svg class="close-btn" viewBox="0 0 42 42" aria-label="Close">
      <path d="M4 4L38 38M38 4L4 38" stroke="#fff" stroke-width="5.5" stroke-linecap="round"/>
    </svg>
    <h1 class="sheet-title">Create Post</h1>
    <div class="visibility-toggle">
      <span class="visibility-label">Private</span>
      <span class="visibility-dot"></span>
    </div>
  </section>

  <div class="post-input">
    <span class="caret"></span>
    <span class="placeholder">Share a New Post</span>
    <svg class="expand-icon" viewBox="0 0 42 42" fill="none" stroke="#8fa0d0" stroke-width="2.5" stroke-linecap="round">
      <path d="M24 18L38 4M28 4H38V14M18 24L4 38M4 28V38H14"/>
    </svg>
  </div>

  <svg class="tool tool-media" width="78" height="58" viewBox="0 0 78 58" aria-label="Add media">
    <rect x="12" y="2" width="64" height="44" rx="4" fill="none" stroke="var(--icon-blue)" stroke-width="5"/>
    <rect x="2" y="12" width="64" height="44" rx="4" fill="var(--icon-blue)"/>
    <path d="M8 50L24 32L36 44L46 36L60 50Z" fill="#fff"/>
    <circle cx="50" cy="24" r="5" fill="#fff"/>
  </svg>
  <svg class="tool tool-place" width="56" height="66" viewBox="0 0 56 66" aria-label="Add location">
    <path d="M28 2C14 2 4 12 4 26C4 42 28 64 28 64S52 42 52 26C52 12 42 2 28 2Z" fill="var(--brand-pink)"/>
    <circle cx="28" cy="26" r="14" fill="#fff"/>
    <path d="M28 34L20 26C17 23 19 18 23 18C25.5 18 27 20 28 21C29 20 30.5 18 33 18C37 18 39 23 36 26Z" fill="var(--brand-pink)"/>
  </svg>
  <svg class="tool tool-tag" width="64" height="64" viewBox="0 0 64 64" aria-label="Add tag">
    <path d="M4 6V28L36 60L62 34L30 2H8C6 2 4 4 4 6Z" fill="var(--icon-blue)"/>
    <circle cx="16" cy="14" r="5" fill="#fff"/>
    <path d="M38 44L28 34C25 31 27 25 32 25C35 25 36.5 27 38 28.5C39.5 27 41 25 44 25C49 25 51 31 48 34Z" fill="#fff"/>
  </svg>

  <div class="send-btn" aria-label="Send">
    <svg width="54" height="54" viewBox="0 0 54 54">
      <path d="M50 4L4 22L22 30L30 50Z" fill="none" stroke="#fff" stroke-width="5" stroke-linejoin="round"/>
      <path d="M50 4L22 30" stroke="#fff" stroke-width="5" stroke-linecap="round"/>
    </svg>
  </div>
</body>
</html>
```